Webdesign für Bau von Wohnanlagen aus Containermodulen
Zielgruppe
Wir bauen Wohnanlagen, Bürogebäude, Kindergärten, Schulen etc. aus einzelnen Containermodulen - übernehmen die Montage, Umbau und Versetzung, Reparaturen und Einlagerungen. Unsere Zielgruppe sind überwiegend Firmen und Kommunen. Der Text für die Homepage ist bereits fertig. Hier erhalten Sie weitere Informationen über unser Tätigkeitsfeld.
Aufgabenstellung
Die Farbe unseres Logos ist blau. Sie sollte sich natürlich in der Homepage minimal widerspiegeln, aber nicht dominieren. Bilder sollten nicht zu klein gehalten werden. Wir möchten dadurch zeigen, was möglich ist (z.B. Umsetzungen von ganzen Containeranlagen am Stück - hier haben wir eine Monopolstellung).

```html
<!DOCTYPE html>
<html lang="de">
<head>
<meta charset="utf-8">
<title>VELDOR Montagearbeiten</title>
<link href="https://fonts.googleapis.com/css2?family=Poppins:wght@500;600;700&family=Work+Sans:wght@400;500;600&display=swap" rel="stylesheet">
<style>
:root{
  --blue:#1c2a8e;
  --blue-mid:#2f46a9;
  --yellow:#f7b10c;
  --ink:#222;
  --text:#7a7a7a;
  --light-num:#e6e6e6;
  --contact:#67709f;
  --white:#fff;
}
*{margin:0;padding:0;box-sizing:border-box}
html,body{width:1200px;height:3148px;overflow:hidden}
body{position:relative;background:var(--white);font-family:"Work Sans",sans-serif;color:var(--text)}
.abs{position:absolute}
.heading{font-family:"Poppins",sans-serif}

/* header */
.site-header{top:0;left:0;width:1200px;height:61px;background:var(--white);border-bottom:1px solid #e5e5e5}
.brand{left:233px;top:9px;display:flex;align-items:center;gap:8px}
.brand-square{width:20px;height:20px;background:var(--blue)}
.brand-name{font-family:"Poppins",sans-serif;font-weight:700;font-size:15px;color:var(--blue);letter-spacing:.5px;line-height:1.05}
.main-nav{left:435px;top:24px;display:flex;gap:18px;font-family:"Poppins",sans-serif;font-weight:500;font-size:10px;color:#333;letter-spacing:.3px}
.main-nav .active{color:var(--blue)}
.search-btn{left:939px;top:18px;width:26px;height:26px;border-radius:50%;background:#111;display:flex;align-items:center;justify-content:center}

/* hero */
.hero{top:61px;left:0;width:1200px;height:532px;background:linear-gradient(180deg,#2a3893 0%,#24318a 55%,#1f2b7e 100%)}
.hero-kicker{left:235px;top:216px;color:var(--yellow);font-size:14px}
.hero-title{left:235px;top:245px;color:var(--white);font-family:"Poppins",sans-serif;font-weight:700;font-size:30px;line-height:39px;letter-spacing:-.3px}
.btn{display:inline-flex;align-items:center;justify-content:center;font-family:"Poppins",sans-serif;font-weight:500;font-size:8.5px;letter-spacing:.6px}
.hero-btn-primary{left:235px;top:347px;width:92px;height:27px;background:var(--yellow);color:var(--white)}
.hero-btn-ghost{left:333px;top:347px;width:81px;height:27px;border:1.5px solid var(--white);color:var(--white)}
.slider-arrow{top:277px;width:40px;height:40px;border:1px solid rgba(255,255,255,.55);border-radius:50%}
.slider-dots{left:584px;top:549px;display:flex;gap:7px;align-items:center}
.dot{width:5px;height:5px;border-radius:50%;background:var(--yellow)}
.dot.current{width:8px;height:8px;background:none;border:1px solid var(--yellow)}

/* intro */
.intro-label{left:233px;top:727px;width:146px;text-align:right;font-family:"Poppins",sans-serif;font-weight:600;font-size:9.5px;line-height:17px;color:var(--blue);letter-spacing:.3px}
.intro-rule{left:346px;top:780px;width:33px;height:2px;background:var(--blue)}
.intro-text{left:407px;top:725px;width:180px;font-size:11px;line-height:20px;color:var(--text)}
.btn-outline-blue{border:1.5px solid var(--blue);color:var(--blue)}
.intro-btn{left:407px;top:941px;width:111px;height:31px}
.intro-photo{left:632px;top:687px;width:568px;height:311px;background:linear-gradient(160deg,#dfe4e6 0%,#b7bdc2 55%,#8c9095 100%)}

/* services */
.services{top:1121px;left:0;width:1200px;height:450px}
.svc-photo{left:0;top:0;width:300px;height:450px;background:linear-gradient(180deg,#cfd6dc 0%,#9ea3a8 50%,#7d766c 100%)}
.svc-intro{left:300px;top:0;width:300px;height:450px;background:var(--blue-mid);text-align:center}
.svc-title{position:absolute;left:0;top:46px;width:300px;color:var(--yellow);font-family:"Poppins",sans-serif;font-weight:700;font-size:19px;line-height:28px}
.svc-text{position:absolute;left:40px;top:124px;width:220px;color:var(--white);font-size:11.5px;line-height:19px}
.svc-btn{position:absolute;left:104px;top:371px;width:94px;height:31px;border:1.5px solid var(--yellow);color:var(--yellow)}
.tile{width:300px;height:225px;background:linear-gradient(160deg,#5e636b 0%,#3f434a 100%)}
.tile-label{position:absolute;left:0;right:0;bottom:27px;text-align:center;color:var(--white);font-family:"Poppins",sans-serif;font-weight:600;font-size:12px;letter-spacing:.3px}
.tile-label span{color:var(--yellow);margin-left:14px}

/* features */
.feature-photo{width:340px;height:376px}
.f1-photo{left:233px;top:1664px;background:linear-gradient(180deg,#b9b4a8 0%,#2c2c2c 40%,#1d1d1d 70%,#9a9a9a 100%)}
.f2-photo{left:624px;top:2153px;background:linear-gradient(180deg,#c9d6e2 0%,#e4e6e4 30%,#3f6a39 60%,#4b4b4f 100%)}
.f-num{font-family:"Poppins",sans-serif;font-weight:600;font-size:42px;color:var(--light-num);line-height:1}
.f-title{font-family:"Poppins",sans-serif;font-weight:600;font-size:20px}
.f-text{font-size:9.8px;line-height:16px;width:290px}
.f1-num{left:607px;top:1737px}
.f1-title{left:607px;top:1803px;color:var(--yellow)}
.f1-text{left:609px;top:1851px}
.f1-btn{left:608px;top:1933px;width:94px;height:31px;border:1.5px solid var(--yellow);color:var(--yellow)}
.f2-num{left:489px;top:2226px;width:100px;text-align:right}
.f2-title{left:389px;top:2292px;width:200px;text-align:right;color:var(--blue)}
.f2-text{left:299px;top:2340px;text-align:right}
.f2-btn{left:496px;top:2421px;width:93px;height:31px}

/* testimonial */
.testimonial{top:2615px;left:0;width:1200px;height:315px;background:linear-gradient(180deg,#4d4d4f 0%,#3b3b3d 100%)}
.t-title{left:0;top:2674px;width:1200px;text-align:center;color:var(--white);font-family:"Poppins",sans-serif;font-weight:700;font-size:19px;letter-spacing:.5px}
.avatar{left:346px;top:2767px;width:78px;height:69px;background:#d8d8d8}
.t-rule{left:346px;top:2848px;width:18px;height:1px;background:#ddd}
.t-name{left:346px;top:2858px;color:var(--white);font-family:"Poppins",sans-serif;font-weight:600;font-size:8.5px}
.t-role{left:346px;top:2871px;color:#ddd;font-size:8.5px;font-style:italic}
.t-quote{left:468px;top:2772px;width:392px;color:#ddd;font-size:10px;line-height:19px}
.t-arrow{top:2789px;width:25px;height:25px;border:1px solid rgba(255,255,255,.6);display:flex;align-items:center;justify-content:center}

/* contact */
.contact{top:2930px;left:0;width:1200px;height:178px;background:var(--contact)}
.contact-item{top:2988px;width:180px;text-align:center;color:var(--white);font-size:10.5px;line-height:17px}
.contact-item svg{display:block;margin:0 auto 18px}

/* footer */
.site-footer{top:3108px;left:0;width:1200px;height:40px;background:var(--blue);color:var(--white);font-size:8.5px}
.copyright{left:233px;top:15px}
.footer-nav{right:235px;top:15px;display:flex;gap:16px}
</style>
</head>
<body>

<header class="site-header abs">
  <div class="brand abs">
    <div class="brand-square"></div>
    <div class="brand-name">VELDOR<br>MONTAGEARBEITEN</div>
  </div>
  <nav class="main-nav abs">
    <span class="active">HOME</span><span>LEISTUNGEN</span><span>WIR ÜBER UNS</span><span>REFERENZEN</span><span>AKTUELLES</span><span>KONTAKT</span><span>IMPRESSUM</span>
  </nav>
  <div class="search-btn abs">
    <svg width="10" height="10" viewBox="0 0 10 10"><circle cx="4" cy="4" r="3" fill="none" stroke="#fff" stroke-width="1.4"/><line x1="6.2" y1="6.2" x2="9" y2="9" stroke="#fff" stroke-width="1.4"/></svg>
  </div>
</header>

<section class="hero abs" role="img" aria-label="Mehrstöckige Containeranlage mit Treppen und Balkonen vor einem Altbau, blau eingefärbt"></section>
<p class="hero-kicker abs">Dem Container-Service</p>
<h1 class="hero-title abs">HERZLICH WILLKOMMEN<br>BEI VELDOR MONTAGEARBEITEN</h1>
<span class="btn hero-btn-primary abs">KONTAKTIERE UNS</span>
<span class="btn hero-btn-ghost abs">WIR ÜBER UNS</span>
<div class="slider-arrow abs" style="left:49px"><svg width="40" height="40" viewBox="0 0 40 40"><polyline points="22,16 18,20 22,24" fill="none" stroke="#fff" stroke-width="1"/></svg></div>
<div class="slider-arrow abs" style="left:1109px"><svg width="40" height="40" viewBox="0 0 40 40"><polyline points="18,16 22,20 18,24" fill="none" stroke="#fff" stroke-width="1"/></svg></div>
<div class="slider-dots abs"><span class="dot"></span><span class="dot current"></span><span class="dot"></span></div>

<section class="intro">
  <p class="intro-label abs">PROFESSIONELLE<br>UND GARANTIERTE ARBEIT</p>
  <div class="intro-rule abs"></div>
  <p class="intro-text abs">VELDOR Montagearbeiten – maßgeschneiderte Lösungen für temporäre Containeranlagen. Wir schaffen mobilen Raum. Profitieren Sie von unserer langjährigen Erfahrung!</p>
  <span class="btn btn-outline-blue intro-btn abs">ERFAHREN SIE MEHR</span>
  <div class="intro-photo abs" role="img" aria-label="Zweistöckige graue Containeranlage mit Außentreppe"></div>
</section>

<section class="services abs">
  <div class="svc-photo abs" role="img" aria-label="Containeranlage mit Lastwagen und Ladekran auf einer Baustelle"></div>
  <div class="svc-intro abs">
    <h2 class="svc-title">UNSERE<br>DIENSTLEISTUNGEN</h2>
    <p class="svc-text">Gerne bieten wir Ihnen maßgeschneiderte Lösungen für Ihre Probleme an. Mit uns können Sie rechnen unsere Kalkulationen sind fair und nachvollziehbar</p>
    <span class="btn svc-btn">MEHR WISSEN</span>
  </div>
  <div class="tile abs" style="left:600px;top:0" role="img" aria-label="Containermodul hängt am Kran bei der Montage"><p class="tile-label">MONTAGE<span>›</span></p></div>
  <div class="tile abs" style="left:900px;top:0" role="img" aria-label="Ganze Containereinheit wird am Kran versetzt"><p class="tile-label">UMBAU UND VERSETZUNG<span>›</span></p></div>
  <div class="tile abs" style="left:600px;top:225px;background:linear-gradient(160deg,#8a8d90 0%,#5b5e62 100%)" role="img" aria-label="Innenraum eines Containers mit Deckenplatten"><p class="tile-label">REPARATUR<span>›</span></p></div>
  <div class="tile abs" style="left:900px;top:225px;background:linear-gradient(160deg,#7a7e84 0%,#4a4d52 100%)" role="img" aria-label="Einzelner Container am Kranhaken"><p class="tile-label">EINLAGERUNG<span>›</span></p></div>
</section>

<section class="feature">
  <div class="feature-photo f1-photo abs" role="img" aria-label="Schwarze zweistöckige Containeranlage als Geschäftsstelle vor historischer Fassade"></div>
  <p class="f-num f1-num abs">01</p>
  <h3 class="f-title f1-title abs">Kommerziell Geschäftsstelle</h3>
  <p class="f-text f1-text abs">Lorem ipsum dolor sit amet, consectetur adipisicing elit, sed do eiusmod tempor incididunt ut labore et dolore magna aliqua. Ut enim ad minim veniam.</p>
  <span class="btn f1-btn abs">MEHR WISSEN</span>
</section>

<section class="feature">
  <p class="f-num f2-num abs">02</p>
  <h3 class="f-title f2-title abs">Wohnung</h3>
  <p class="f-text f2-text abs">Lorem ipsum dolor sit amet, consectetur adipisicing elit, sed do eiusmod tempor incididunt ut labore et dolore magna aliqua. Ut enim ad minim veniam.</p>
  <span class="btn btn-outline-blue f2-btn abs">MEHR WISSEN</span>
  <div class="feature-photo f2-photo abs" role="img" aria-label="Tribünenanlage aus Containern mit Dachkonstruktion am Kran"></div>
</section>

<section class="testimonial abs" role="img" aria-label="Belebte Einkaufsstraße, abgedunkelt"></section>
<h2 class="t-title abs">ZEUGNIS</h2>
<div class="t-arrow abs" style="left:259px"><svg width="8" height="8" viewBox="0 0 8 8"><polyline points="5,1 2,4 5,7" fill="none" stroke="#fff"/></svg></div>
<div class="avatar abs" role="img" aria-label="Platzhalter Kundenporträt"></div>
<div class="t-rule abs"></div>
<p class="t-name abs">JONAS REIF</p>
<p class="t-role abs">Kunde</p>
<p class="t-quote abs">Lorem ipsum dolor sit amet, consectetur adipisicing elit, sed do eiusmod tempor incididunt ut labore et dolore magna aliqua. Ut enim ad minim veniam, quis nostrud exercitation ullamco laboris nisi ut aliquip.</p>
<div class="t-arrow abs" style="left:914px"><svg width="8" height="8" viewBox="0 0 8 8"><polyline points="3,1 6,4 3,7" fill="none" stroke="#fff"/></svg></div>

<section class="contact abs"></section>
<div class="contact-item abs" style="left:330px">
  <svg width="20" height="24" viewBox="0 0 20 24"><path d="M10 23 C10 23 2 14 2 9 A8 8 0 0 1 18 9 C18 14 10 23 10 23Z" fill="none" stroke="#fff" stroke-width="1.1"/><circle cx="10" cy="9" r="3" fill="none" stroke="#fff" stroke-width="1.1"/></svg>
  Lindenweg 12<br>72815 Auenbach
</div>
<div class="contact-item abs" style="left:513px">
  <svg width="24" height="24" viewBox="0 0 24 24"><path d="M5 3 L9 3 L10 8 L7.5 10 C9 13.5 11 15.5 14 17 L16 14.5 L21 15.5 L21 19.5 C21 20.5 20 21 19 21 C10 20.5 3.5 14 3 5 C3 4 4 3 5 3Z" fill="none" stroke="#fff" stroke-width="1.1"/></svg>
  07231-554820
</div>
<div class="contact-item abs" style="left:696px">
  <svg width="24" height="24" viewBox="0 0 24 24"><rect x="1.5" y="5" width="21" height="14" fill="none" stroke="#fff" stroke-width="1.1"/><polyline points="1.5,5 12,13 22.5,5" fill="none" stroke="#fff" stroke-width="1.1"/><line x1="1.5" y1="19" x2="9" y2="11.5" stroke="#fff" stroke-width="1.1"/><line x1="22.5" y1="19" x2="15" y2="11.5" stroke="#fff" stroke-width="1.1"/></svg>
  info@veldor-montage.de
</div>

<footer class="site-footer abs">
  <p class="copyright abs">© 2017 VELDOR MONTAGEARBEITEN – Alle Rechte vorbehalten</p>
  <nav class="footer-nav abs"><span>Home</span><span>Leistungen</span><span>Wir über uns</span><span>Referenzen</span><span>Aktuelles</span><span>Kontakt</span><span>Impressum</span></nav>
</footer>

</body>
</html>
```